Crestline Gas and Plumbing Business Card Design

I am after a business card design for my plumbing business called 'Crestline Gas & Plumbing'. I do all types of plumbing and gas work and specialise in general maintenance plumbing. Would like to see designs using current logo

Industry/Entity Type

Plumbing

Contact Information for Business Card

Name - Dale Whitcombe
Phone number - 0455163027
Email - admin@crestlinegasandplumbing.example.com.au
ABN - 68204915336

```html
<!DOCTYPE html>
<html lang="en">
<head>
<meta charset="utf-8">
<title>Crestline Gas &amp; Plumbing – Business Cards</title>
<link href="https://fonts.googleapis.com/css2?family=Open+Sans:wght@400;600;700&display=swap" rel="stylesheet">
<style>
  :root {
    --backdrop: #d5d5d5;
    --navy: #2b3597;
    --blue: #1f6fbf;
    --band-dark: #2b2b2b;
    --orange: #f7a531;
    --flame: #e9432f;
    --ink: #2d2d2d;
    --white: #ffffff;
    --brand-blue: #1d63c0;
  }
  * { box-sizing: border-box; margin: 0; padding: 0; }
  html, body {
    width: 1200px; height: 900px; overflow: hidden;
    background: var(--backdrop);
    font-family: "Open Sans", Arial, sans-serif;
  }
  .sheet {
    width: 1200px; height: 900px;
    display: flex; flex-direction: column; align-items: center; justify-content: center;
    gap: 44px;
  }
  .card {
    position: relative;
    width: 680px; height: 388px;
    overflow: hidden;
    box-shadow: 0 6px 18px rgba(0,0,0,0.18);
  }
  .card-art { position: absolute; inset: 0; }

  /* Back side */
  .back-brand {
    position: absolute; left: 0; right: 0; top: 150px;
    display: flex; align-items: center; justify-content: center; gap: 14px;
  }
  .brand-dot {
    width: 34px; height: 34px; border-radius: 50%;
    background: var(--orange);
  }
  .brand-name {
    font-weight: 700; font-size: 30px; color: var(--brand-blue);
    letter-spacing: 0.5px;
  }
  .back .brand-name { color: var(--white); }
  .back-web {
    position: absolute; left: 0; right: 0; bottom: 52px;
    text-align: center; color: var(--white);
    font-size: 17px; letter-spacing: 1.2px;
  }

  /* Front side */
  .front { background: var(--white); }
  .front-brand {
    position: absolute; left: 40px; top: 44px;
    display: flex; align-items: center; gap: 12px;
  }
  .front .brand-name { font-size: 26px; }
  .person { position: absolute; left: 40px; top: 150px; }
  .person-name { color: var(--brand-blue); font-weight: 600; font-size: 24px; }
  .person-role { color: var(--ink); font-size: 16px; margin-top: 2px; }
  .contacts {
    position: absolute; left: 40px; top: 232px;
    list-style: none; color: var(--ink); font-size: 15.5px; line-height: 25px;
  }
  .contacts li { display: flex; align-items: center; gap: 10px; }
  .contacts svg { width: 14px; height: 14px; flex: none; }
  .abn {
    position: absolute; left: 40px; bottom: 11px;
    font-size: 17px; color: var(--white); letter-spacing: 0.3px;
  }
  .abn-label { color: var(--orange); }
</style>
</head>
<body>
<main class="sheet">

  <section class="card back" aria-label="Business card back">
    <svg class="card-art" viewBox="0 0 680 388" preserveAspectRatio="none" aria-hidden="true">
      <defs>
        <linearGradient id="skyGrad" x1="0" y1="0" x2="1" y2="1">
          <stop offset="0" stop-color="#2c3696"/>
          <stop offset="0.6" stop-color="#2b3a9c"/>
          <stop offset="1" stop-color="#1274c0"/>
        </linearGradient>
        <linearGradient id="fireGrad" x1="0" y1="0" x2="1" y2="1">
          <stop offset="0" stop-color="#fbb92f"/>
          <stop offset="0.5" stop-color="#f58a35"/>
          <stop offset="1" stop-color="#e8352f"/>
        </linearGradient>
      </defs>
      <rect x="0" y="0" width="680" height="194" fill="url(#skyGrad)"/>
      <rect x="0" y="194" width="680" height="194" fill="url(#fireGrad)"/>
      <polygon points="0,118 80,118 120,92 560,92 600,118 680,118 680,270 600,270 560,296 120,296 80,270 0,270"
               fill="var(--band-dark)"/>
      <polygon points="0,118 80,118 120,92 560,92 600,118 680,118" fill="none" stroke="#ffffff" stroke-width="3"/>
      <polygon points="0,270 80,270 120,296 560,296 600,270 680,270" fill="none" stroke="#ffffff" stroke-width="3"/>
    </svg>
    <div class="back-brand">
      <span class="brand-dot" aria-hidden="true"></span>
      <span class="brand-name">Crestline Gas &amp; Plumbing</span>
    </div>
    <p class="back-web">www.crestlinegasandplumbing.example.com.au</p>
  </section>

  <section class="card front" aria-label="Business card front">
    <svg class="card-art" viewBox="0 0 680 388" preserveAspectRatio="none" aria-hidden="true">
      <defs>
        <linearGradient id="stripGrad" x1="0" y1="0" x2="1" y2="0">
          <stop offset="0" stop-color="#2b2f95"/>
          <stop offset="0.6" stop-color="#2a45a8"/>
          <stop offset="1" stop-color="#1a74c2"/>
        </linearGradient>
      </defs>
      <polygon points="0,350 420,350 436,334 680,334 680,388 0,388" fill="url(#stripGrad)"/>
    </svg>

    <div class="front-brand">
      <span class="brand-dot" aria-hidden="true"></span>
      <span class="brand-name">Crestline Gas &amp; Plumbing</span>
    </div>

    <div class="person">
      <p class="person-name">Dale Whitcombe</p>
      <p class="person-role">Founder</p>
    </div>

    <ul class="contacts">
      <li>
        <svg viewBox="0 0 16 16" aria-hidden="true"><path d="M3.5 1.5l2.5 0 1 3.5-1.8 1.2a8 8 0 0 0 4.6 4.6L11 9l3.5 1v2.5c0 1-1 2-2 2C6.5 14.5 1.5 9.5 1.5 3.5c0-1 1-2 2-2z" fill="var(--orange)"/></svg>
        0455163027
      </li>
      <li>
        <svg viewBox="0 0 16 16" aria-hidden="true"><rect x="1.5" y="3.5" width="13" height="9" fill="none" stroke="var(--orange)" stroke-width="1.6"/><path d="M1.5 3.5l6.5 5 6.5-5" fill="none" stroke="var(--orange)" stroke-width="1.6"/></svg>
        admin@crestlinegasandplumbing.example.com.au
      </li>
      <li>
        <svg viewBox="0 0 16 16" aria-hidden="true"><circle cx="8" cy="8" r="6.5" fill="none" stroke="var(--orange)" stroke-width="1.5"/><path d="M1.5 8h13M8 1.5c-3 3.5-3 9.5 0 13M8 1.5c3 3.5 3 9.5 0 13" fill="none" stroke="var(--orange)" stroke-width="1.2"/></svg>
        www.crestlinegasandplumbing.example.com.au
      </li>
    </ul>

    <p class="abn"><span class="abn-label">ABN:</span> 68204915336</p>
  </section>

</main>
</body>
</html>
```